TRV Business Card

Business card design for a handyman company. Want to portray a professional image and stay away from the "Mom & Pops" image that is normally associated with handyman companies.

Business

```html
<!DOCTYPE html>
<html lang="en">
<head>
<meta charset="utf-8">
<title>TRV Business Card</title>
<link rel="stylesheet" href="https://fonts.googleapis.com/css2?family=Questrial&family=Archivo:wght@700&display=swap">
<style>
  :root {
    --navy: #0b1f3a;
    --white: #ffffff;
    --stage: #e8e8e8;
  }
  * { margin: 0; padding: 0; box-sizing: border-box; }
  html, body { width: 1200px; height: 1000px; overflow: hidden; background: var(--stage); }
  body { position: relative; font-family: "Questrial", sans-serif; color: var(--navy); }

  .card {
    position: absolute; top: 350px; width: 516px; height: 302px;
    background: var(--white); overflow: hidden;
  }
  .card--front { left: 72px; }
  .card--back { left: 622px; }

  .front-panel { position: absolute; left: 0; top: 0; }

  .name-plate {
    position: absolute; left: 31px; top: 33px; width: 267px; height: 92px;
    background: var(--white); border-radius: 18px;
    display: flex; align-items: center; justify-content: center;
  }
  .brand-name {
    font-family: "Questrial", sans-serif; font-size: 60px; line-height: 1;
    color: var(--navy); letter-spacing: 4px;
  }

  .services { position: absolute; left: 25px; top: 148px; color: var(--white); }
  .services__title { font-size: 16px; margin-bottom: 6px; }
  .services__list { list-style: none; }
  .services__item { font-size: 15px; line-height: 22px; display: flex; align-items: center; }
  .services__item::before {
    content: ""; width: 7px; height: 7px; background: var(--white); margin-right: 6px;
  }

  .divider { position: absolute; left: 338px; top: 45px; width: 2px; height: 58px; background: var(--navy); }
  .address { position: absolute; left: 371px; top: 58px; font-size: 14px; line-height: 20px; }

  .contacts { position: absolute; right: 22px; top: 150px; font-size: 14px; }
  .contacts__row { display: flex; justify-content: flex-end; align-items: center; height: 26px; }
  .contacts__row svg { margin-left: 8px; width: 14px; height: 14px; fill: var(--navy); }

  .tagline {
    font-family: "Archivo", sans-serif; font-weight: 700; font-size: 14.5px;
    color: var(--navy); letter-spacing: 0.2px; white-space: nowrap;
  }
  .card--front .tagline {
    position: absolute; left: 207px; top: 262px;
    font-size: 13.6px; letter-spacing: 0;
  }

  .band { position: absolute; top: 131px; width: 91px; height: 41px; background: var(--navy); }
  .band--left { left: 0; }
  .band--right { right: 0; }
  .back-name {
    position: absolute; left: 0; right: 0; top: 95px; text-align: center;
  }
  .back-name .brand-name { font-size: 64px; }
  .card--back .tagline { position: absolute; left: 0; right: 0; top: 187px; text-align: center; }
</style>
</head>
<body>
  <section class="card card--front">
    <svg class="front-panel" width="200" height="302" viewBox="0 0 200 302">
      <path d="M0 0 H146 Q170 0 172 28 L181 130 L196 268 Q198 302 164 302 H0 Z" fill="var(--navy)"/>
    </svg>
    <div class="name-plate"><span class="brand-name">TRV</span></div>

    <div class="services">
      <p class="services__title">Potential Verbage</p>
      <ul class="services__list">
        <li class="services__item">Home Repairs</li>
        <li class="services__item">Handyman</li>
        <li class="services__item">Services</li>
        <li class="services__item">Drain Cleaning</li>
        <li class="services__item">Carpet Cleaning</li>
      </ul>
    </div>

    <div class="divider"></div>
    <p class="address">2750 W Meadow Ln<br>Harlow, Ks 66190</p>

    <div class="contacts">
      <div class="contacts__row">(555) 318-4620
        <svg viewBox="0 0 16 16"><path d="M1 6 Q8 1 15 6 L13 8 L11 6.5 L11 5 Q8 4 5 5 L5 6.5 L3 8 Z M4 9 H12 L13 14 H3 Z"/></svg>
      </div>
      <div class="contacts__row">(555) 318-4621
        <svg viewBox="0 0 16 16"><path d="M4 1 H12 V5 H4 Z M1 6 H15 V12 H12 V10 H4 V12 H1 Z M5 11 H11 V15 H5 Z"/></svg>
      </div>
      <div class="contacts__row">office@TRVservices.com
        <svg viewBox="0 0 16 16"><path d="M1 3 H15 V4 L8 9 L1 4 Z M1 5.5 L8 10.5 L15 5.5 V13 H1 Z"/></svg>
      </div>
    </div>

    <p class="tagline">RESIDENTIAL &amp; COMMERCIAL SERVICES</p>
  </section>

  <section class="card card--back">
    <div class="band band--left"></div>
    <div class="band band--right"></div>
    <div class="back-name"><span class="brand-name">TRV</span></div>
    <p class="tagline">RESIDENTIAL &amp; COMMERCIAL SERVICES</p>
  </section>
</body>
</html>
```